Clever & creative business card needed for a pediatric dentist.

We need a business card for a pediatric dentist that is building a brand-new pediatric dental practice. He is funny, outgoing, and sociable, and he hopes to give his business card to dentists and pediatricians so that he can give them information of where to refer infants, children, and teenagers that need high quality and attainable dental care.

The name of the dental practice is Copper Fern Pediatric Dentistry. Logo design .png / .pdf/ .jpg are provided to aid in the design.

The dentist's last name is Tolvan (which sounds like "burger", as in "hamburger” or “cheeseburger"). Since it is pediatric practice, kudos will be given to designs that implement a little joke into the design - but hopefully in a small or hidden way (such as putting something like a cheeseburger on the back of the card, or hiding it an an abstract way).

Thank you!

Please make a design that incorporates colors. It should be fun! Not too serious. It does not have to follow the color scheme of the logos.

```html
<!DOCTYPE html>
<html lang="en">
<head>
<meta charset="utf-8">
<title>Copper Fern Pediatric Dentistry – Business Card</title>
<link rel="stylesheet" href="https://fonts.googleapis.com/css2?family=Montserrat:wght@500&family=Heebo:wght@400;800&display=swap">
<style>
  :root {
    --backdrop: #bfbfbf;
    --paper: #ffffff;
    --mint-pale: #e3f1e3;
    --mint: #cbe8cd;
    --mint-deep: #b3dcba;
    --mint-mid: #9fd6a8;
    --green: #3aa862;
    --ink: #3e3e3e;
    --ink-soft: #444444;
  }
  * { box-sizing: border-box; margin: 0; padding: 0; }
  html, body {
    width: 1100px;
    height: 1200px;
    overflow: hidden;
    background: var(--backdrop);
  }
  .sheet {
    position: relative;
    width: 1100px;
    height: 1200px;
  }
  .card {
    position: absolute;
    left: 100px;
    width: 900px;
    height: 514px;
    background: var(--paper);
    box-shadow: 0 4px 10px rgba(0, 0, 0, 0.22);
    overflow: hidden;
  }
  .card--front {
    top: 60px;
    background:
      radial-gradient(ellipse 260px 200px at 60px 470px, var(--mint) 0%, rgba(227, 241, 227, 0) 100%),
      radial-gradient(ellipse 300px 240px at 870px 40px, var(--mint-pale) 0%, rgba(227, 241, 227, 0) 100%),
      radial-gradient(ellipse 420px 320px at 120px 120px, #f1f7f1 0%, rgba(241, 247, 241, 0) 100%),
      var(--paper);
  }
  .card--back { top: 626px; }

  .brand {
    position: absolute;
    left: 0;
    right: 0;
    text-align: center;
    font-family: "Montserrat", sans-serif;
    font-weight: 500;
    color: var(--ink);
  }
  .brand__dot {
    display: block;
    margin: 0 auto;
    border-radius: 50%;
    background: var(--mint-mid);
  }
  .brand__name {
    display: block;
    line-height: 1;
    letter-spacing: 0.01em;
  }
  .brand__tag {
    display: block;
    text-transform: uppercase;
  }

  .card--front .brand { top: 118px; }
  .card--front .brand__dot { width: 112px; height: 112px; margin-bottom: 28px; }
  .card--front .brand__name { font-size: 52px; }
  .card--front .brand__tag { font-size: 16px; letter-spacing: 0.42em; margin-top: 12px; padding-left: 0.42em; }

  .site {
    position: absolute;
    top: 410px;
    left: 0;
    right: 0;
    text-align: center;
    font-family: "Heebo", sans-serif;
    font-weight: 400;
    font-size: 27px;
    letter-spacing: 0.13em;
    color: var(--ink);
  }

  .back-art {
    position: absolute;
    left: 0;
    top: 0;
    width: 380px;
    height: 514px;
    background:
      radial-gradient(ellipse 300px 380px at 60px 380px, var(--mint-deep) 0%, rgba(203, 232, 205, 0.6) 50%, rgba(255, 255, 255, 0) 100%),
      radial-gradient(ellipse 320px 260px at 140px 80px, var(--mint-pale) 0%, rgba(227, 241, 227, 0) 100%);
  }

  .back-info {
    position: absolute;
    left: 470px;
    width: 360px;
    top: 56px;
    text-align: center;
  }
  .back-info .brand { position: static; }
  .back-info .brand__dot { width: 96px; height: 96px; margin-bottom: 16px; }
  .back-info .brand__name { font-size: 40px; }
  .back-info .brand__tag { font-size: 13px; letter-spacing: 0.38em; margin-top: 8px; padding-left: 0.38em; }

  .person {
    margin-top: 18px;
    font-family: "Heebo", sans-serif;
    line-height: 1.05;
  }
  .person__name {
    font-weight: 800;
    font-size: 36px;
    color: var(--green);
    letter-spacing: -0.01em;
  }
  .person__role {
    font-weight: 400;
    font-size: 23px;
    color: var(--ink-soft);
  }

  .contact {
    list-style: none;
    margin-top: 40px;
    font-family: "Heebo", sans-serif;
    font-weight: 400;
    font-size: 23px;
    color: var(--ink-soft);
  }
  .contact__item + .contact__item { margin-top: 12px; }
  .contact__icon {
    display: block;
    margin: 0 auto 4px;
    fill: var(--green);
  }
</style>
</head>
<body>
<main class="sheet">

  <section class="card card--front" aria-label="Card front">
    <div class="brand">
      <span class="brand__dot" aria-hidden="true"></span>
      <span class="brand__name">copper fern</span>
      <span class="brand__tag">Pediatric Dentistry</span>
    </div>
    <p class="site">www.copperfern.com</p>
  </section>

  <section class="card card--back" aria-label="Card back">
    <div class="back-art" role="img" aria-label="Soft green area holding a faint hidden cheeseburger sketch"></div>

    <div class="back-info">
      <div class="brand">
        <span class="brand__dot" aria-hidden="true"></span>
        <span class="brand__name">copper fern</span>
        <span class="brand__tag">Pediatric Dentistry</span>
      </div>
      <div class="person">
        <p class="person__name">TOLVAN</p>
        <p class="person__role">Pediatric Dentist</p>
      </div>
      <ul class="contact">
        <li class="contact__item">
          <svg class="contact__icon" width="18" height="18" viewBox="0 0 24 24" aria-hidden="true">
            <path d="M6.6 10.8a15.1 15.1 0 0 0 6.6 6.6l2.2-2.2a1 1 0 0 1 1-.25 11.4 11.4 0 0 0 3.6.57 1 1 0 0 1 1 1V20a1 1 0 0 1-1 1A17 17 0 0 1 3 4a1 1 0 0 1 1-1h3.5a1 1 0 0 1 1 1c0 1.250.2 2.45.57 3.570a1 1 0 0 1-.25 1z"/>
          </svg>
          +123 555 0189
        </li>
        <li class="contact__item">
          <svg class="contact__icon" width="18" height="14" viewBox="0 0 24 18" aria-hidden="true">
            <path d="M0 0h24v2.2L12 10 0 2.2z"/>
            <path d="M0 4.6l12 7.8 12-7.8V18H0z"/>
          </svg>
          info@copperfern.com
        </li>
      </ul>
    </div>
  </section>

</main>
</body>
</html>
```